Special offers flyer for IT firm

We need a flyer design for our IT technical services firm based in Melbourne, Australia. We want to advertise two offerings on a double sided flyer.
-
First Offering:
Free computer system health report and audit
- health check of servers, workstations and network
- comprehensive non-technical report including recommendations
-
Second Offering:
Discounted technical support - $80* per hour
- day to day helpdesk support
- system upgrades and migrations
- cloud services design, implementation and support
- web hosting, domain names and email filtering

*exclusive of GST (must denote somewhere in small print)
-
The contact details for the offer must include room for Phone, Email and Web Address.

I am not set on the text, or any particular format, additional images would be good to break up the pages.

Target Market(s)

Professional Services small business owners (under 30 staff)

Industry/Entity Type

Computer

Requirements
Must have
• DL Sized document (210mmx99mm) portrait or landscape, double sided.

```html
<!DOCTYPE html>
<html lang="en">
<head>
<meta charset="utf-8">
<title>Tarnvale IT – Special Offers Flyers</title>
<link rel="stylesheet" href="https://fonts.googleapis.com/css2?family=Tinos:wght@400;700&family=Arimo:wght@400&display=swap">
<style>
  :root {
    --backdrop: #a6a6a6;
    --paper: #ffffff;
    --ink: #231f20;
    --brand-blue: #1f64a6;
    --text-light: #ffffff;
    --logo-shadow: #c9c9c9;
  }
  * { box-sizing: border-box; margin: 0; padding: 0; }
  html, body { width: 1200px; height: 900px; overflow: hidden; }
  body { background: var(--backdrop); position: relative; font-family: "Tinos", "Times New Roman", serif; }

  .flyer {
    position: absolute; top: 40px; width: 385px; height: 820px;
    background: var(--paper);
    box-shadow: 8px 8px 8px rgba(0,0,0,0.45);
  }
  .flyer--front { left: 162px; }
  .flyer--back { left: 643px; }

  .flyer__header { position: absolute; top: 0; left: 0; width: 100%; height: 218px; }
  .brand-name {
    position: absolute; top: 85px; width: 100%; text-align: center;
    font-family: "Tinos", "Times New Roman", serif; font-weight: 400;
    font-size: 62px; color: var(--ink); letter-spacing: 1px; line-height: 1;
    white-space: nowrap;
  }
  .brand-underglow {
    position: absolute; top: 194px; left: 72px; width: 74px; height: 8px;
    border-radius: 50%; background: var(--logo-shadow); opacity: .7;
  }

  .flyer__body {
    position: absolute; top: 218px; left: 0; width: 100%; height: 508px;
    background: var(--ink); color: var(--text-light);
    border-top: 12px solid var(--brand-blue);
    border-bottom: 14px solid var(--brand-blue);
    font-weight: 700;
  }
  .offer-line { position: absolute; left: 0; width: 100%; text-align: center; line-height: 1; white-space: nowrap; }
  .bullet { position: absolute; white-space: nowrap; }
  .bullet--front { font-size: 24px; line-height: 28px; }
  .bullet--back { font-size: 23px; line-height: 27px; }
  .small-print { position: absolute; left: 30px; top: 457px; font-size: 15px; font-weight: 400; }

  .headline-free { top: 38px; font-size: 104px; }
  .front-sub-1 { top: 153px; font-size: 35px; padding-left: 10px; }
  .front-sub-2 { top: 191px; font-size: 35px; }

  .headline-discount { top: 38px; font-size: 49px; }
  .back-sub-1 { top: 101px; font-size: 38px; }
  .back-sub-2 { top: 148px; font-size: 38px; }

  .flyer__footer {
    position: absolute; bottom: 0; right: 10px; width: 100%; padding-top: 6px;
    height: 94px; text-align: right;
    font-family: "Arimo", Arial, sans-serif; font-size: 18.5px; line-height: 26px; color: var(--ink);
  }
</style>
</head>
<body>

  <section class="flyer flyer--front" aria-label="Free health report offer">
    <header class="flyer__header">
      <div class="brand-name">Tarnvale IT</div>
      <div class="brand-underglow"></div>
    </header>
    <div class="flyer__body">
      <div class="offer-line headline-free">FREE</div>
      <div class="offer-line front-sub-1">Computer system health</div>
      <div class="offer-line front-sub-2">report and audit</div>
      <div class="bullet bullet--front" style="left:24px; top:256px;">- health check of servers,<br>workstation and network</div>
      <div class="bullet bullet--front" style="left:17px; top:325px;">&nbsp;- comprehensive non-technical<br>report including reccomendations</div>
    </div>
    <footer class="flyer__footer">
      02 5550 1234<br>hello@tarnvaleit.example<br>www.tarnvaleit.example
    </footer>
  </section>

  <section class="flyer flyer--back" aria-label="Discounted support offer">
    <header class="flyer__header">
      <div class="brand-name">Tarnvale IT</div>
      <div class="brand-underglow"></div>
    </header>
    <div class="flyer__body">
      <div class="offer-line headline-discount">DISCOUNTED</div>
      <div class="offer-line back-sub-1">Technical support</div>
      <div class="offer-line back-sub-2">$80* per hour</div>
      <div class="bullet bullet--back" style="left:28px; top:203px;">- Day to day helpdesk support</div>
      <div class="bullet bullet--back" style="left:33px; top:244px;">- System upgrades and migrations</div>
      <div class="bullet bullet--back" style="left:30px; top:283px;">- cloud services design,<br>implementation and support</div>
      <div class="bullet bullet--back" style="left:27px; top:341px;">&nbsp;- Web hosting, domain names and<br>email filtering</div>
      <div class="small-print">*Exclusive of GST</div>
    </div>
    <footer class="flyer__footer">
      02 5550 1234<br>hello@tarnvaleit.example<br>www.tarnvaleit.example
    </footer>
  </section>

</body>
</html>
```